Fernmoor PTA Website Design

We are working with Fernmoor Elementary School PTA. They are a Parent Teacher Association that needs a new website design.

A Parent Teacher Association (PTA) is a volunteer organization that brings parents, teachers, and school staff together to support students and enhance their educational experience. PTAs organize fundraisers, sponsor school events, advocate for education policies, and foster stronger connections between families and schools.

Some sites to use for inspiration:

https://clubvane.com/demo/
https://nonprofits.fundrova.com/blogs/more-great-pta-websites-you-should-copy
https://www.qerbrix.com

Thank you for taking the time to consider designing a website for us. We are web developers based in Stockton and Los Angeles, CA, USA. Most of our projects go through the same process. Understanding this process may help you win a project with us. We custom-code all of our websites in-house. We don’t have any requirements as to what tools you use for your design, but we prefer Figma files. For any design that we label as four-stars, we send it to the client for review. The client picks the final design they want us to use. Once we complete this process, we will continue to show additional clients all the four-star sites and purchase them later. Your designs will have multiple chances to sell. For better chances of success, we ask that you follow these guidelines.

IMAGES:
If you use any images or icons in the design, we ask that you have a link to the asset so we can purchase the image/icon. Most of the designs we submit do not have the customer’s images on them unless they have some great images. Be creative; show us the feeling you are trying to portray with your image choices. Use any royalty-free site you choose. We subscribe to Vexiq and mainly use their images, but we can purchase images outside of Vexiq.

PLEASE NOTE: we will not submit designs to clients with watermarks on the images.

FONTS:
We ask that you identify the fonts used in the design. This can be done in a message if you want. We typically use Tarnel Fonts and Vexiq Fonts.

CONTENT:
We're always open to different content and ideas. We often submit designs with stock images so the client can see our vision. We typically take pictures after the website launch to use their images with our vision. Lorem Ipsum is fine for paragraphs, but we ask that you write the headers in correct English. We want to be able to show the vision and identify the sections of the website.

INSPIRATION:
We typically add a couple of links in the brief of websites we like to help you get started in your design.

REVISIONS:
We do not often ask for revisions of the designs unless we see something in the design that may not appeal to the client. If there are slight changes that we want to make, we do that in the development process.

FEEDBACK:
We rarely give feedback on designs during the design process. We are working on many website projects and do not have the time to provide feedback. We usually respond if your request is well thought out and asks specific questions, but a note asking “feedback, please” usually goes unanswered.

```html
<!DOCTYPE html>
<html lang="en">
<head>
<meta charset="utf-8">
<title>Fernmoor PTA</title>
<link href="https://fonts.googleapis.com/css2?family=Rubik:wght@400;500;600&display=swap" rel="stylesheet">
<style>
:root{
  --page:#f8f7f5;
  --navy:#213d8c;
  --ink:#141d35;
  --body:#3b4256;
  --beige:#ebe6dc;
  --card:#ffffff;
  --tint:#e6e9f2;
  --footer:#15295a;
  --pill:#eef0f4;
}
*{margin:0;padding:0;box-sizing:border-box}
html,body{width:1200px;height:4165px;overflow:hidden}
body{background:var(--page);font-family:"Rubik",sans-serif;color:var(--body);position:relative}
a{color:inherit;text-decoration:none}
.abs{position:absolute}
.eyebrow{font-size:13px;font-weight:500;letter-spacing:2.4px;color:var(--body);text-transform:uppercase}
.title{font-weight:600;color:var(--ink);line-height:1.15}
.btn{display:inline-flex;align-items:center;justify-content:center;height:39px;padding:0 34px;border-radius:20px;background:var(--navy);color:#fff;font-size:12px;font-weight:600;letter-spacing:2px;text-transform:uppercase}
.ph{border-radius:14px}
.learn{display:flex;align-items:center;gap:10px;font-size:13px;color:var(--body)}
.learn .arrow{width:18px;height:18px;border-radius:50%;background:var(--pill);display:flex;align-items:center;justify-content:center}
.pill{display:inline-block;padding:5px 11px;border-radius:14px;background:var(--pill);font-size:11px;color:var(--body)}

/* nav */
.brand{left:100px;top:30px;display:flex;align-items:center;gap:10px;font-size:24px;font-weight:600;color:var(--navy)}
.brand .mark{width:22px;height:22px;background:var(--navy);border-radius:4px}
.nav{left:440px;top:24px;display:flex;gap:36px;font-size:13px;color:var(--ink)}
.nav a.active{position:relative;color:var(--navy)}
.nav a.active::after{content:"";position:absolute;left:-3px;right:-3px;bottom:-8px;height:2px;border-radius:2px;background:var(--navy)}

/* hero */
.hero-title{left:100px;top:214px;font-size:48px}
.hero-text{left:100px;top:346px;width:320px;font-size:14.5px;line-height:1.7}
.hero-btn{left:100px;top:445px}
.hero-art{left:440px;top:130px;width:760px;height:581px;background:linear-gradient(180deg,#f8f7f5 0%,#e7e9ee 45%,#c9d3e8 75%,#f3f3f1 100%);border-radius:0}

/* about */
.about{left:50px;top:733px;width:1100px;height:567px;background:var(--beige);border-radius:26px}
.about .eyebrow{position:absolute;left:66px;top:78px}
.about .title{position:absolute;left:66px;top:104px;font-size:36px}
.about p{position:absolute;left:66px;top:206px;width:408px;font-size:14px;line-height:1.72}
.about .btn{position:absolute;left:66px;top:451px}
.about .photo{position:absolute;left:550px;top:66px;width:484px;height:435px;background:linear-gradient(135deg,#5d6675,#2f4a8f 55,#8a7a90);background:linear-gradient(135deg,#6b7280 0%,#2f4a8f 55%,#a17e95 100%);border-radius:16px}

/* events */
.events-head{left:0;top:1402px;width:1200px;text-align:center}
.events-head .title{font-size:36px;margin-top:10px}
.event{top:1560px;width:311px;height:440px;background:var(--card);border-radius:16px;box-shadow:0 2px 14px rgba(20,29,53,.05)}
.event .thumb{position:absolute;left:20px;top:20px;width:271px;height:199px;background:var(--tint);border-radius:4px}
.event .pill{position:absolute;left:20px;top:240px}
.event h3{position:absolute;left:20px;top:275px;font-size:20px;font-weight:500;color:var(--ink)}
.event p{position:absolute;left:20px;top:311px;width:270px;font-size:12.5px;line-height:1.7;height:64px;overflow:hidden}
.event .learn{position:absolute;left:20px;top:400px}

/* support */
.oval{border-radius:50%/42%}
.lion{left:89px;top:2138px;width:247px;height:427px;background:var(--tint);border-radius:124px}
.lion .inner{position:absolute;inset:12px;border-radius:112px;background:linear-gradient(180deg,#2f4a8f,#213d8c)}
.kids{left:362px;top:2194px;width:249px;height:421px;background:#fff;border-radius:125px;box-shadow:0 0 0 1px #eceae6}
.kids .inner{position:absolute;inset:12px;border-radius:113px;background:linear-gradient(160deg,#b79a86,#6d6a72 60%,#3e3c48)}
.support{left:702px;top:2206px;width:420px}
.support .title{font-size:36px;margin-top:12px}
.support p{margin-top:22px;font-size:14px;line-height:1.74}
.support .btn{margin-top:24px;padding:0 27px}

/* news */
.news{left:34px;top:2722px;width:1132px;height:781px;background:var(--beige);border-radius:26px}
.news .eyebrow{position:absolute;left:66px;top:66px}
.news .head{position:absolute;left:66px;top:98px;font-size:36px}
.news .art{position:absolute;left:791px;top:27px;width:129px;height:125px;background:radial-gradient(circle,#dfe3ee 0%,rgba(235,230,220,0) 70%);border-radius:50%}
.news .all{position:absolute;right:70px;top:116px;font-size:13px}
.news-card{background:var(--card);border-radius:16px;position:absolute}
.feature{left:66px;top:178px;width:484px;height:536px}
.feature .thumb{position:absolute;left:26px;top:27px;width:430px;height:267px;background:linear-gradient(180deg,#a9c4e6 0%,#6f9b5a 45%,#58606e 75%,#7d7f85 100%);border-radius:4px}
.feature .pill{position:absolute;left:26px;top:318px}
.feature h3{position:absolute;left:26px;top:353px;font-size:20px;font-weight:500;color:var(--ink)}
.feature p{position:absolute;left:26px;top:386px;width:430px;font-size:12.5px;line-height:1.7;height:44px;overflow:hidden}
.feature .learn{position:absolute;left:26px;top:490px}
.mini{left:582px;width:484px;height:253px}
.mini .thumb{position:absolute;left:28px;top:27px;width:139px;height:199px;border-radius:4px}
.mini .body{position:absolute;left:188px;top:27px;width:270px}
.mini h3{margin-top:13px;font-size:20px;font-weight:500;color:var(--ink)}
.mini p{margin-top:14px;font-size:12.5px;line-height:1.7}
.mini .learn{position:absolute;left:188px;bottom:28px}

/* footer */
.footer{left:0;top:3603px;width:1200px;height:562px;background:var(--footer);color:#dfe5f3}
.footer .cta{position:absolute;left:100px;top:66px;font-size:33px;font-weight:600;color:#fff;line-height:1.2}
.footer .btn{position:absolute;left:100px;top:167px;background:#fff;color:var(--navy);padding:0 32px}
.footer .brand{position:absolute;left:100px;top:310px;color:#fff;font-size:22px}
.footer .brand .mark{background:#fff}
.footer .addr{position:absolute;left:202px;top:276px;font-size:12.5px;line-height:1.7}
.footer .social{position:absolute;left:202px;top:354px;display:flex;gap:20px}
.footer .social span{width:19px;height:19px;border-radius:50%;border:2px solid #fff}
.footer .ql{position:absolute;left:632px;top:278px;font-size:13px;color:#fff}
.footer .col{position:absolute;top:325px;display:flex;flex-direction:column;gap:25px;font-size:13px}
.footer .col a{display:flex;align-items:center;gap:8px}
.footer .col .ext{width:18px;height:18px;border-radius:50%;background:#c8d0e3;display:flex;align-items:center;justify-content:center}
.footer .copy{position:absolute;left:100px;top:510px;font-size:12px;display:flex;gap:18px}
</style>
</head>
<body>

<header>
  <a class="abs brand" href="#"><span class="mark"></span>Fernmoor</a>
  <nav class="abs nav">
    <a class="active" href="#">Home</a>
    <a href="#">Programs &amp; Events
      <svg width="9" height="6" viewBox="0 0 9 6"><path d="M1 1l3.5 3.5L8 1" fill="none" stroke="#141d35" stroke-width="1.4"/></svg></a>
    <a href="#">Support</a>
    <a href="#">Store</a>
    <a href="#">Contact</a>
  </nav>
</header>

<section>
  <h1 class="abs title hero-title">Welcome to<br>Fernmoor PTA</h1>
  <p class="abs hero-text">Join a community of leaders that embraces effort, exhibits empathy, and celebrates diversity.</p>
  <a class="abs btn hero-btn" href="#">Join now</a>
  <div class="abs hero-art" role="img" aria-label="Sketched illustration of the school entrance sign with trees and a flagpole"></div>
</section>

<section class="abs about">
  <div class="eyebrow">About</div>
  <h2 class="title">How Fernmoor PTA<br>Supports Students</h2>
  <p>Together with families and staff, Fernmoor PTA funds and organizes the extras that feel essential - field trips, arts and STEM enrichments, assemblies, and community events that lift every classroom. By pairing volunteer power with smart budgeting, we extend learning beyond the bell and strengthen a welcoming school culture for all students. Your participation whether joining, donating, or volunteering directly turns plans into programs kids love and remember.</p>
  <a class="btn" href="#">Learn more</a>
  <div class="photo" role="img" aria-label="Photo of PTA volunteers holding donated backpacks"></div>
</section>

<section>
  <div class="abs events-head">
    <div class="eyebrow">Events</div>
    <h2 class="title">Upcoming Events &amp;<br>Programs</h2>
  </div>
  <article class="abs event" style="left:100px">
    <div class="thumb" role="img" aria-label="Line illustration for the fall carnival"></div>
    <span class="pill">Oct 25, 2025</span>
    <h3>2024 Fall Carnival</h3>
    <p>Join the fun and support the Fernmoor 6th Graders! Carnival games, tasty food, yummy treats and loads of fun are just a few of the things waiting for you.</p>
    <a class="learn" href="#">Learn more <span class="arrow"><svg width="8" height="8" viewBox="0 0 8 8"><path d="M1.5 6.5l5-5M2.5 1.5h4v4" fill="none" stroke="#213d8c" stroke-width="1.2"/></svg></span></a>
  </article>
  <article class="abs event" style="left:445px">
    <div class="thumb" role="img" aria-label="Line illustration of a yearbook"></div>
    <span class="pill">Oct 1, 2025</span>
    <h3>Fernmoor Yearbook</h3>
    <p>Parents, students, family and friends! Break out that camera and snap those pics! 1st day of school, Red Ribbon Week, class parties and more.</p>
    <a class="learn" href="#">Learn more <span class="arrow"><svg width="8" height="8" viewBox="0 0 8 8"><path d="M1.5 6.5l5-5M2.5 1.5h4v4" fill="none" stroke="#213d8c" stroke-width="1.2"/></svg></span></a>
  </article>
  <article class="abs event" style="left:789px">
    <div class="thumb" role="img" aria-label="Line illustration of a picnic basket"></div>
    <span class="pill">May 3, 2025</span>
    <h3>Spring Picnic</h3>
    <p>Friday, May 3 is our annual Spring Picnic supporting the next 6th grade class! Join us for a fantastic Star Voyagers-themed evening.</p>
    <a class="learn" href="#">Learn more <span class="arrow"><svg width="8" height="8" viewBox="0 0 8 8"><path d="M1.5 6.5l5-5M2.5 1.5h4v4" fill="none" stroke="#213d8c" stroke-width="1.2"/></svg></span></a>
  </article>
</section>

<section>
  <div class="abs lion"><div class="inner" role="img" aria-label="Mascot artwork"></div></div>
  <div class="abs kids"><div class="inner" role="img" aria-label="Photo of smiling students"></div></div>
  <div class="abs support">
    <div class="eyebrow">Support</div>
    <h2 class="title">Support Fernmoor<br>Lions</h2>
    <p>PTA works hard to provide an incredible array of programs and experiences for all our Fernmoor Lions! With an operating budget of approximately $50,000 per year, your support is pivotal to ensuring all our Lions can experience field trips, monthly art lessons, STEM experiments, assemblies, drama program opportunities and more. Please join us by giving back!</p>
    <a class="btn" href="#">Donate</a>
  </div>
</section>

<section class="abs news">
  <div class="eyebrow">News</div>
  <h2 class="title head">PTA News &amp; Updates</h2>
  <div class="art" role="img" aria-label="Line illustration of tin-can telephones"></div>
  <a class="learn all" href="#">View all news <span class="arrow"><svg width="8" height="8" viewBox="0 0 8 8"><path d="M1.5 6.5l5-5M2.5 1.5h4v4" fill="none" stroke="#213d8c" stroke-width="1.2"/></svg></span></a>

  <article class="news-card feature">
    <div class="thumb" role="img" aria-label="Photo of the school fence banner beside the street"></div>
    <span class="pill">Nov 14, 2025</span>
    <h3>Thursday Newsletter</h3>
    <p>Highlights from this week, including upcoming event dates, volunteer signups, and quick links to RSVP for events, sign up to volunteer and more.</p>
    <a class="learn" href="#">Learn more <span class="arrow"><svg width="8" height="8" viewBox="0 0 8 8"><path d="M1.5 6.5l5-5M2.5 1.5h4v4" fill="none" stroke="#213d8c" stroke-width="1.2"/></svg></span></a>
  </article>

  <article class="news-card mini" style="top:178px">
    <div class="thumb" role="img" aria-label="Photo of students at back to school night" style="background:linear-gradient(160deg,#c9a98f,#6f7fa8 60%,#3b4a78)"></div>
    <div class="body">
      <span class="pill">Oct 11, 2025</span>
      <h3>Back to School Night</h3>
      <p>Meet teachers, tour classrooms, and get calendars and signups for fall programs; details inside.</p>
    </div>
    <a class="learn" href="#">Learn more <span class="arrow"><svg width="8" height="8" viewBox="0 0 8 8"><path d="M1.5 6.5l5-5M2.5 1.5h4v4" fill="none" stroke="#213d8c" stroke-width="1.2"/></svg></span></a>
  </article>

  <article class="news-card mini" style="top:460px">
    <div class="thumb" role="img" aria-label="Photo of parents gathered in the library" style="background:linear-gradient(170deg,#c8c2b4,#7d7668 55%,#3f3b38)"></div>
    <div class="body">
      <span class="pill">Sep 22, 2025</span>
      <h3>First PTA Member Meeting</h3>
      <p style="margin-top:48px">Join us in the library from 6:00–7:00 pm to hear program updates and ways to get involved this semester.</p>
    </div>
    <a class="learn" href="#">Learn more <span class="arrow"><svg width="8" height="8" viewBox="0 0 8 8"><path d="M1.5 6.5l5-5M2.5 1.5h4v4" fill="none" stroke="#213d8c" stroke-width="1.2"/></svg></span></a>
  </article>
</section>

<footer class="abs footer">
  <h2 class="cta">Every Voice Matters, Join<br>Fernmoor PTA</h2>
  <a class="btn" href="#">Join now</a>
  <a class="brand" href="#"><span class="mark"></span></a>
  <div class="addr">1480 Alder Crest Lane<br>Brookvale, CA 95012<br>(555) 014-2286</div>
  <div class="social" aria-label="Social links"><span></span><span></span><span></span></div>
  <div class="ql">Quick Links</div>
  <div class="col" style="left:632px">
    <a href="#">Programs &amp; Events</a>
    <a href="#">Support</a>
    <a href="#">Store</a>
  </div>
  <div class="col" style="left:841px;top:323px">
    <a href="#">Contact</a>
    <a href="#">Fernmoor Elementary <span class="ext"><svg width="8" height="8" viewBox="0 0 8 8"><path d="M1.5 6.5l5-5M2.5 1.5h4v4" fill="none" stroke="#15295a" stroke-width="1.2"/></svg></span></a>
  </div>
  <div class="copy"><span>Copyright © 2025 Fernmoor PTA. All rights reserved.</span><span>Terms&nbsp;&nbsp;&nbsp;Privacy</span></div>
</footer>

</body>
</html>
```